Stationery Design Project - New innovative law firm

I need a simple design, yet the tone of the stationery set need to express modern, professionalism, smart and forward-thinking. I don’t need a business card, but require the stationery set to have:
• Design letterhead
• Design facsimile
• Design memo
The triangular logo with Halvard Lane words etc, need to be present in the stationery. The red triangular logo should not be re-designed, but feel free to play around with the placement and colours of the Halvard Lane words etc....?

Target Market(s)

Business clients

Industry/Entity Type

Business

Requirements
Must have
• The triangular logo with Halvard Lane words etc...for branding.

```html
<!DOCTYPE html>
<html lang="en">
<head>
<meta charset="utf-8">
<title>Halvard Lane — Letterhead</title>
<link rel="stylesheet" href="https://fonts.googleapis.com/css2?family=Open+Sans:wght@400;700&family=Arimo:wght@400;700&display=swap">
<style>
  :root {
    --paper: #ffffff;
    --tint-light: #eeeeee;
    --tint-mid: #e1e1e1;
    --tint-dark: #d8d8d8;
    --brand-red: #d9261c;
    --ink: #231f20;
    --ink-soft: #3c3c3c;
  }
  html, body {
    margin: 0;
    padding: 0;
    overflow: hidden;
    background: var(--paper);
  }
  .letterhead {
    position: relative;
    width: 917px;
    height: 1200px;
    overflow: hidden;
    background: var(--paper);
  }
  .backdrop {
    position: absolute;
    inset: 0;
    width: 917px;
    height: 1200px;
  }
  .backdrop .tint-light { fill: var(--tint-light); }
  .backdrop .tint-mid { fill: var(--tint-mid); }
  .backdrop .tint-dark { fill: var(--tint-dark); }
  .backdrop .sheet { fill: var(--paper); }
  .backdrop .accent { fill: var(--brand-red); }

  .brand {
    position: absolute;
    left: 62px;
    top: 56px;
    display: flex;
    align-items: center;
    gap: 16px;
  }
  .brand-mark {
    width: 60px;
    height: 60px;
    background: var(--brand-red);
  }
  .brand-name {
    margin: 0;
    font-family: "Open Sans", Arial, sans-serif;
    font-weight: 700;
    font-size: 30px;
    line-height: 1;
    letter-spacing: 0.5px;
    color: var(--ink);
    text-transform: uppercase;
  }
  .brand-tagline {
    margin: 5px 0 0;
    font-family: "Open Sans", Arial, sans-serif;
    font-weight: 400;
    font-size: 12.5px;
    line-height: 1;
    color: var(--ink-soft);
    text-transform: uppercase;
  }

  .contact {
    position: absolute;
    left: 166px;
    top: 1090px;
    margin: 0;
    font-family: "Arimo", Arial, sans-serif;
    font-size: 12.5px;
    line-height: 18.5px;
    color: var(--ink-soft);
  }
  .contact dt {
    display: inline;
    font-weight: 700;
    color: var(--ink);
  }
  .contact dd {
    display: inline;
    margin: 0 0 0 3px;
  }
  .contact-row { display: block; }
</style>
</head>
<body>
  <main class="letterhead">
    <svg class="backdrop" viewBox="0 0 917 1200" aria-hidden="true">
      <rect class="tint-light" x="0" y="0" width="917" height="1200"/>
      <polygon class="tint-dark" points="500,0 917,0 917,33 584,193"/>
      <polygon class="tint-mid" points="584,193 917,33 917,920"/>
      <polygon class="sheet" points="0,464 584,193 917,920 917,1200 171,1200 0,827"/>
      <polygon class="accent" points="407,1200 917,963 917,1200"/>
    </svg>

    <header class="brand">
      <div class="brand-mark" aria-hidden="true"></div>
      <div class="brand-text">
        <h1 class="brand-name">Halvard Lane</h1>
        <p class="brand-tagline">Accounting, Tax, Business Advice &amp; Legal</p>
      </div>
    </header>

    <dl class="contact">
      <div class="contact-row"><dt>Address:</dt><dd>27 Marlow Street, Kedron Park, QLD 4031</dd></div>
      <div class="contact-row"><dt>Mobile:</dt><dd>+61 400 172 665</dd></div>
      <div class="contact-row"><dt>E-mail:</dt><dd>m.ellis@halvardlane.com.au</dd></div>
      <div class="contact-row"><dt>Web:</dt><dd>www.halvardlane.com.au</dd></div>
    </dl>
  </main>
</body>
</html>
```